Copperfield Provisions Company Label

I need a label designed that will reflect the Copperfield Provisions Company. We produce and source locally meat products such as sausages, pates, terrines, mousses etc.... The label needs to communicate artistry, modernism, hand made, playfulness. We produce the finest meat products and utilize only locally sourced meat from the best farmers. All these things we hold in high regard and it needs to be reflected in the label. The label must also have a vintage feel since we are using vintage techniques of production. The first image file is my companies logo and should be used as a jumping off point.
Should be no larger then 4"x 4", I dont have specifics on shape i am open to anything. The packaging is ROP (reduced oxygen packaging) sometimes called cyo-vac packaging.
Please yield to the images i posted as inspiration in the direction i want. The logo does not have to be used, but i would like it in the same vein of design. Again artistry and graphics.
Target Market(s)
Consumer who care about the products they are consuming. These people frequent farmers markets and have a tend to buy locally even when it is more expensive.
Industry/Entity Type
It Company
Requirements
Must have
- Vintage imagery and a modern feel, a red and black color scheme. Other colors will be acceptable in the right taste. A statement of weight, use any for this case. Must have a place for the contents of the package, "Grass Fed Hot Dogs" for example.
Nice to have
- A old timely friendly butcher, a hand crank meat grinder, wooden butcher tables, cleavers.
Should not have
- Animal silhouettes

```html
<!DOCTYPE html>
<html lang="en">
<head>
<meta charset="UTF-8">
<title>Grass Fed Hot Dogs Label</title>
<link rel="stylesheet" href="https://fonts.googleapis.com/css2?family=Oswald:wght@500&family=PT+Sans:wght@700&family=Roboto+Condensed:wght@700&display=swap">
<style>
  :root {
    --backdrop: #ededed;
    --paper: #ffffff;
    --butcher-red: #d91f26;
    --ink-black: #111111;
    --iron-grey: #4a4a4a;
    --stripe-grey: #595959;
    --pale-stripe: #c9c9c9;
    --caption-grey: #3f3f3f;
  }
  html, body {
    margin: 0;
    width: 1200px;
    height: 1200px;
    overflow: hidden;
    background: var(--backdrop);
  }
  .label {
    position: absolute;
    left: 274px;
    top: 225px;
    width: 653px;
    height: 750px;
    display: block;
  }
  .label-paper { fill: var(--paper); }
  .outer-frame { fill: none; stroke: var(--butcher-red); stroke-width: 10; stroke-linejoin: miter; }
  .inner-frame { fill: none; stroke: var(--ink-black); stroke-width: 4; stroke-linejoin: miter; }
  .side-chevron { fill: none; stroke: var(--butcher-red); stroke-width: 9; stroke-linejoin: miter; }
  .side-stripe { fill: var(--stripe-grey); }
  .base-stripe { fill: var(--pale-stripe); }
  .origin-line {
    font-family: "PT Sans", sans-serif;
    font-weight: 700;
    font-size: 23px;
    fill: var(--caption-grey);
  }
  .origin-rule { stroke: var(--caption-grey); stroke-width: 2.5; }
  .product-name {
    font-family: "Oswald", sans-serif;
    font-weight: 500;
    font-size: 78px;
    fill: var(--butcher-red);
  }
  .weight-badge { fill: var(--iron-grey); }
  .weight-badge-edge { fill: none; stroke: var(--paper); stroke-width: 1.5; }
  .weight-text {
    font-family: "Roboto Condensed", sans-serif;
    font-weight: 700;
    font-size: 27px;
    fill: var(--paper);
  }
</style>
</head>
<body>
<svg class="label" viewBox="0 0 544 625" xmlns="http://www.w3.org/2000/svg" aria-label="Grass Fed Hot Dogs label">
  <defs>
    <clipPath id="side-field">
      <polygon points="8,60 88,310 8,560"/>
    </clipPath>
    <clipPath id="inner-field">
      <polygon points="30,30 514,30 420,310 514,595 30,595 124,310"/>
    </clipPath>
    <linearGradient id="grinder-tone" x1="0" y1="0" x2="1" y2="1">
      <stop offset="0" stop-color="#e4e4e4"/>
      <stop offset="0.55" stop-color="#8c8c8c"/>
      <stop offset="1" stop-color="#3e3e3e"/>
    </linearGradient>
  </defs>

  <rect class="label-paper" x="0" y="0" width="544" height="625"/>

  <g class="side-panel side-panel-left">
    <g clip-path="url(#side-field)">
      <rect class="side-stripe" x="12" y="0" width="5" height="625"/>
      <rect class="side-stripe" x="24" y="0" width="5" height="625"/>
      <rect class="side-stripe" x="36" y="0" width="5" height="625"/>
      <rect class="side-stripe" x="48" y="0" width="5" height="625"/>
      <rect class="side-stripe" x="60" y="0" width="5" height="625"/>
      <rect class="side-stripe" x="72" y="0" width="5" height="625"/>
    </g>
    <polyline class="side-chevron" points="30,115 96,310 30,505"/>
  </g>

  <g class="side-panel side-panel-right" transform="translate(544 0) scale(-1 1)">
    <g clip-path="url(#side-field)">
      <rect class="side-stripe" x="12" y="0" width="5" height="625"/>
      <rect class="side-stripe" x="24" y="0" width="5" height="625"/>
      <rect class="side-stripe" x="36" y="0" width="5" height="625"/>
      <rect class="side-stripe" x="48" y="0" width="5" height="625"/>
      <rect class="side-stripe" x="60" y="0" width="5" height="625"/>
      <rect class="side-stripe" x="72" y="0" width="5" height="625"/>
    </g>
    <polyline class="side-chevron" points="30,115 96,310 30,505"/>
  </g>

  <g class="base-band" clip-path="url(#inner-field)">
    <rect class="base-stripe" x="40" y="492" width="3" height="90"/>
    <rect class="base-stripe" x="48" y="492" width="3" height="90"/>
    <rect class="base-stripe" x="56" y="492" width="3" height="90"/>
    <rect class="base-stripe" x="64" y="492" width="3" height="90"/>
    <rect class="base-stripe" x="72" y="492" width="3" height="90"/>
    <rect class="base-stripe" x="80" y="492" width="3" height="90"/>
    <rect class="base-stripe" x="88" y="492" width="3" height="90"/>
    <rect class="base-stripe" x="96" y="492" width="3" height="90"/>
    <rect class="base-stripe" x="104" y="492" width="3" height="90"/>
    <rect class="base-stripe" x="112" y="492" width="3" height="90"/>
    <rect class="base-stripe" x="120" y="492" width="3" height="90"/>
    <rect class="base-stripe" x="128" y="492" width="3" height="90"/>
    <rect class="base-stripe" x="136" y="492" width="3" height="90"/>
    <rect class="base-stripe" x="144" y="492" width="3" height="90"/>
    <rect class="base-stripe" x="152" y="492" width="3" height="90"/>
    <rect class="base-stripe" x="160" y="492" width="3" height="90"/>
    <rect class="base-stripe" x="168" y="492" width="3" height="90"/>
    <rect class="base-stripe" x="176" y="492" width="3" height="90"/>
    <rect class="base-stripe" x="184" y="492" width="3" height="90"/>
    <rect class="base-stripe" x="192" y="492" width="3" height="90"/>
    <rect class="base-stripe" x="200" y="492" width="3" height="90"/>
    <rect class="base-stripe" x="208" y="492" width="3" height="90"/>
    <rect class="base-stripe" x="216" y="492" width="3" height="90"/>
    <rect class="base-stripe" x="224" y="492" width="3" height="90"/>
    <rect class="base-stripe" x="232" y="492" width="3" height="90"/>
    <rect class="base-stripe" x="240" y="492" width="3" height="90"/>
    <rect class="base-stripe" x="248" y="492" width="3" height="90"/>
    <rect class="base-stripe" x="256" y="492" width="3" height="90"/>
    <rect class="base-stripe" x="264" y="492" width="3" height="90"/>
    <rect class="base-stripe" x="272" y="492" width="3" height="90"/>
    <rect class="base-stripe" x="280" y="492" width="3" height="90"/>
    <rect class="base-stripe" x="288" y="492" width="3" height="90"/>
    <rect class="base-stripe" x="296" y="492" width="3" height="90"/>
    <rect class="base-stripe" x="304" y="492" width="3" height="90"/>
    <rect class="base-stripe" x="312" y="492" width="3" height="90"/>
    <rect class="base-stripe" x="320" y="492" width="3" height="90"/>
    <rect class="base-stripe" x="328" y="492" width="3" height="90"/>
    <rect class="base-stripe" x="336" y="492" width="3" height="90"/>
    <rect class="base-stripe" x="344" y="492" width="3" height="90"/>
    <rect class="base-stripe" x="352" y="492" width="3" height="90"/>
    <rect class="base-stripe" x="360" y="492" width="3" height="90"/>
    <rect class="base-stripe" x="368" y="492" width="3" height="90"/>
    <rect class="base-stripe" x="376" y="492" width="3" height="90"/>
    <rect class="base-stripe" x="384" y="492" width="3" height="90"/>
    <rect class="base-stripe" x="392" y="492" width="3" height="90"/>
    <rect class="base-stripe" x="400" y="492" width="3" height="90"/>
    <rect class="base-stripe" x="408" y="492" width="3" height="90"/>
    <rect class="base-stripe" x="416" y="492" width="3" height="90"/>
    <rect class="base-stripe" x="424" y="492" width="3" height="90"/>
    <rect class="base-stripe" x="432" y="492" width="3" height="90"/>
    <rect class="base-stripe" x="440" y="492" width="3" height="90"/>
    <rect class="base-stripe" x="448" y="492" width="3" height="90"/>
    <rect class="base-stripe" x="456" y="492" width="3" height="90"/>
    <rect class="base-stripe" x="464" y="492" width="3" height="90"/>
    <rect class="base-stripe" x="472" y="492" width="3" height="90"/>
    <rect class="base-stripe" x="480" y="492" width="3" height="90"/>
    <rect class="base-stripe" x="488" y="492" width="3" height="90"/>
    <rect class="base-stripe" x="496" y="492" width="3" height="90"/>
    <rect class="base-stripe" x="504" y="492" width="3" height="90"/>
  </g>

  <polygon class="outer-frame" points="5,5 539,5 427,310 539,620 5,620 117,310"/>
  <polygon class="inner-frame" points="30,30 514,30 420,310 514,595 30,595 124,310"/>

  <text class="origin-line" x="272" y="76" text-anchor="middle" textLength="238" lengthAdjust="spacingAndGlyphs">LOCALLY PRODUCED</text>
  <line class="origin-rule" x1="152" y1="85" x2="392" y2="85"/>

  <text class="product-name" x="272" y="169" text-anchor="middle" textLength="312" lengthAdjust="spacingAndGlyphs">GRASS FED</text>
  <text class="product-name" x="272" y="240" text-anchor="middle" textLength="292" lengthAdjust="spacingAndGlyphs">HOT DOGS</text>

  <polygon class="grinder-illustration" points="120,260 424,260 411,310 470,492 74,492 133,310" fill="url(#grinder-tone)" role="img" aria-label="Engraved illustration of a vintage hand-crank meat grinder on a wooden butcher table, minced meat falling onto a plate"/>

  <g class="weight-tag">
    <polygon class="weight-badge" points="155,532 170,510 374,510 389,532 374,555 170,555"/>
    <polygon class="weight-badge-edge" points="160,532 173,514 371,514 384,532 371,551 173,551"/>
    <text class="weight-text" x="272" y="542" text-anchor="middle">Weight 1lb</text>
  </g>
</svg>
</body>
</html>
```